Good afternoon,
1. Can we also have the ‘Lanternbugs selections of the month’ moved to the left side and smaller than the logo quote ‘inquisitive minds on adventure’ as it’s just a subheading. That said can we have the ‘Inquisitive minds on adventure’ a little larger.
2. Can we have the order of the drop down menus as. Age then Theme then Location (no price). Next to these titles can we have a small image such as a locator point next to ‘location’, two people holding hands adult and child net to ‘age’ and something adventure/city next to ‘theme’, an image to represent the drop down menus. See below:

3. Can we please use this as a logo instead of what we have at the moment. And the same type of setup as what I have here. I really like this map of Australia. We have the rights to it and I have attached it as a file for you to use.

4. Can the selection buttons all be the same blue as the blue in the logo please. Can every part of the page have the logo blue/dirty orange also? Makes it calmer.

5. Could you please add a ‘calendar’ to the tabs (in blue at the top of the page, on the left of ‘add and activity’ .
Let me know how you go. Thanks

Target Market(s)

• Parents and care-givers
• Teachers
• Children (child-friendly)
• Customers are those who ask the question ‘what am I going to do with my child/ren this week/weekend/month’

Industry/Entity Type

Quote

Number of Pages Required

4 page

Font styles to use
Sans Serif

Requirements
Must have
• An ecommerce website (platform) with a responsive system for IOS and Android
• Easy to navigate, user-friendly clean
Nice to have
• some interactive maps
Should not have
• To much clutter/info

```html
<!DOCTYPE html>
<html lang="en">
<head>
<meta charset="utf-8">
<title>Lanternbugs Melbourne</title>
<link href="https://fonts.googleapis.com/css2?family=Raleway:wght@500;600;700;800&family=Open+Sans:wght@400;600;700&family=Rokkitt:wght@500;700&display=swap" rel="stylesheet">
<style>
:root{
  --orange:#e8900c;
  --blue:#0b4e9e;
  --ink:#2b2b2b;
  --muted:#777777;
  --page:#f1f1f1;
  --column:#f4f4f4;
  --field:#e4e4e4;
  --footer:#3b3b3b;
  --footer-text:#d8d8d8;
  --rule:#c9c9c9;
  --white:#ffffff;
}
*{box-sizing:border-box;margin:0;padding:0}
html,body{width:1200px;height:2817px;overflow:hidden}
body{background:var(--page);font-family:"Open Sans",Arial,sans-serif;color:var(--ink);position:relative}
.abs{position:absolute}
.column{left:160px;top:0;width:880px;height:2498px;background:var(--column);border-left:1px solid #e2e2e2;border-right:1px solid #e2e2e2}

.topbar{left:190px;top:0;width:820px;height:23px;font-size:11px;color:#333;display:flex;justify-content:space-between;align-items:center}
.topbar span{display:flex;align-items:center;gap:5px}

.header{left:197px;top:28px;width:813px;height:60px;background:var(--white);box-shadow:0 1px 4px rgba(0,0,0,.12);display:flex;align-items:center;padding:0 18px}
.brand{display:flex;align-items:center;gap:8px}
.brand-mark{width:34px;height:34px;background:var(--blue);border-radius:3px;flex:none}
.brand-name{font-family:"Raleway",sans-serif;font-weight:800;font-size:25px;line-height:26px;color:var(--orange)}
.brand-tagline{font-family:"Raleway",sans-serif;font-weight:800;font-size:12px;line-height:14px;color:var(--orange)}
.nav{display:flex;gap:18px;margin-left:36px;font-family:"Raleway",sans-serif;font-weight:600;font-size:11px;color:#333;align-items:center}
.nav .active{color:var(--orange)}
.nav .tab-calendar{background:var(--blue);color:var(--white);padding:5px 9px;border-radius:2px}
.subscribe{margin-left:auto;display:flex;align-items:center;gap:9px}
.subscribe .gift{width:26px;height:26px;background:var(--orange);border-radius:3px}
.subscribe b{display:block;font-family:"Raleway",sans-serif;font-size:13px;color:var(--orange);font-weight:700}
.subscribe span{font-size:12px;color:#333}

.finder{left:190px;top:103px;width:820px;height:47px;display:flex;align-items:center;gap:10px}
.finder-q{font-family:"Rokkitt",serif;font-weight:700;font-size:16px;color:#333;display:flex;align-items:center;gap:8px;margin-right:20px}
.select{height:40px;display:flex;align-items:center;gap:7px;padding:0 10px;border-left:1px solid var(--rule);font-size:11px;color:#555}
.select .caret{margin-left:4px;border:4px solid transparent;border-top:5px solid #555;margin-top:5px}
.finder-btn{margin-left:auto;width:104px;height:38px;background:var(--blue);color:var(--white);font-size:12px;font-weight:600;text-align:center;line-height:15px;padding-top:4px;border-radius:2px}

.hero{left:190px;top:158px;width:820px;height:372px;background:linear-gradient(180deg,#c9cfb8 0%,#9aa67a 30%,#d86f98 62%,#c2476f 100%)}
.hero-caption{position:absolute;right:5px;top:190px;width:287px;height:133px;background:rgba(96,40,72,.78);color:var(--white);text-align:center;padding:20px 14px 0}
.hero-caption h2{font-family:"Rokkitt",serif;font-weight:700;font-size:21px;line-height:24px;letter-spacing:.5px}
.hero-caption p{font-size:10.5px;line-height:15px;margin-top:10px}

.divider{left:210px;width:780px;border-top:2px dotted #bdbdbd}

.signup{left:190px;top:584px;width:560px}
.signup h2{font-family:"Raleway",sans-serif;font-weight:700;font-size:24px;color:var(--ink)}
.signup h2 em{font-style:normal;color:var(--orange)}
.signup h3{font-family:"Raleway",sans-serif;font-weight:600;font-size:17px;margin-top:18px}
.signup ul{list-style:none;margin-top:10px}
.signup li{display:flex;align-items:center;gap:16px;font-size:11px;color:#333;height:28px}
.signup-form{display:flex;gap:14px;margin-top:14px}
.signup-form span{height:34px;background:var(--field);font-size:11px;color:#666;padding:10px 12px}
.signup-form .btn{background:var(--blue);color:var(--white);font-weight:600;font-size:12px;width:108px;text-align:center;border-radius:2px}
.mailbox{left:798px;top:610px;width:207px;height:182px;background:linear-gradient(180deg,#f4f4f4 0%,#b9b9b9 55%,#6bb83c 85%,#4f9a28 100%);border-radius:4px}

.promo{top:851px;width:268px;height:116px;display:flex;align-items:center;padding:0 14px;color:var(--white)}
.promo .art{width:92px;height:84px;border-radius:4px;flex:none}
.promo .txt{margin-left:auto;text-align:center;width:140px}
.promo p{font-size:12.5px;line-height:16px}
.promo .pill{display:block;background:var(--white);color:#333;font-size:11px;font-weight:600;height:18px;line-height:18px;margin-top:6px;border-radius:1px;text-align:center}
.promo-blue{left:173px;background:var(--blue)}
.promo-orange{left:464px;background:var(--orange)}
.promo-dark{left:757px;background:#444}
.promo-dark .txt{margin-left:0;text-align:left;width:170px}
.promo-dark h4{font-family:"Rokkitt",serif;font-weight:500;font-size:17px;white-space:nowrap}
.promo-dark p{font-size:11.5px;line-height:14px;margin-top:2px}
.promo-dark .pill{width:128px}
.promo-dark .art{margin-left:auto;width:56px;height:56px;background:linear-gradient(180deg,#f7a93a,#e07a10)}

.section-title{font-family:"Raleway",sans-serif;font-weight:700;font-size:24px;color:var(--ink)}
.section-title em{font-style:normal;color:var(--orange)}
.subheading{font-family:"Raleway",sans-serif;font-weight:600;font-size:12px;color:var(--blue)}

.event{width:253px;height:404px;background:var(--white);box-shadow:0 1px 4px rgba(0,0,0,.12)}
.event .photo{height:184px}
.event .body{padding:16px 18px 0}
.event h3{font-family:"Raleway",sans-serif;font-weight:700;font-size:14px;line-height:18px;color:#222}
.meta{display:flex;gap:8px;font-size:9.5px;color:#555;margin-top:12px;align-items:center;white-space:nowrap}
.meta span{display:flex;align-items:center;gap:3px}
.event p,.blog p{font-size:11px;line-height:19px;color:var(--muted);margin-top:12px}
.more{display:block;font-size:12px;color:var(--orange);margin-top:14px}

.show-more{left:573px;top:1937px;width:54px;height:54px;border-radius:50%;background:#333;color:var(--white);font-size:10px;font-weight:600;text-align:center;line-height:13px;padding-top:14px}

.blog{width:338px;height:361px;background:var(--white);box-shadow:0 1px 4px rgba(0,0,0,.12)}
.blog .photo{height:203px;position:relative}
.date{position:absolute;left:0;top:0;width:44px;height:64px;background:var(--blue);color:var(--white);text-align:center;padding-top:8px}
.date b{display:block;font-size:19px;line-height:22px}
.date span{font-size:12px}
.blog .body{padding:20px 18px 0}
.blog h3{font-family:"Raleway",sans-serif;font-weight:700;font-size:16px;color:#222}

.footer{left:0;top:2498px;width:1200px;height:319px;background:var(--footer);color:var(--footer-text)}
.footer h4{font-family:"Raleway",sans-serif;font-weight:700;font-size:15px;color:var(--white)}
.contact{left:190px;top:38px;width:200px}
.contact ul{margin-top:14px}
.contact li{list-style:none;display:flex;align-items:center;gap:18px;font-size:11px;height:24px}
.contact hr{border:none;border-top:1px solid #5a5a5a;margin:14px 0 0}
.socials{display:flex;gap:8px;margin:18px 0 0 28px}
.socials i{width:18px;height:18px;border-radius:3px;background:#9a9a9a;display:block}
.insta{left:468px;top:38px}
.grid{display:grid;grid-template-columns:repeat(3,73px);gap:4px;margin-top:17px}
.grid div{height:64px}
.widget{left:772px;top:35px;width:240px;height:173px;background:var(--white);color:#333}
.widget .cover{height:92px;background:linear-gradient(135deg,#d7c6a3,#8fae6a 60%,#c98a5a)}
.widget .bar{display:flex;justify-content:space-between;padding:5px 8px;font-size:9px;font-weight:600;background:#f2f2f2}
.widget .bar span{border:1px solid #ccc;padding:1px 5px;background:var(--white)}
.widget p{font-size:9px;padding:7px 8px 4px}
.faces{display:flex;gap:3px;padding:0 8px}
.faces i{width:22px;height:22px;background:#b9a894;display:block}
.foot-rule{left:175px;top:263px;width:850px;border-top:1px solid #555}
.copyright{left:175px;top:280px;font-family:"Rokkitt",serif;font-size:11px;color:#aaa}
</style>
</head>
<body>
<div class="abs column"></div>

<div class="abs topbar">
  <span>info@lanternbugs.com <svg width="11" height="8" viewBox="0 0 11 8"><rect width="11" height="8" fill="#333"/><path d="M0 0l5.5 4.5L11 0" stroke="#fff" fill="none"/></svg></span>
  <span>My Account <svg width="9" height="10" viewBox="0 0 9 10"><circle cx="4.5" cy="2.6" r="2.4" fill="#333"/><path d="M0 10c0-3.5 9-3.5 9 0z" fill="#333"/></svg></span>
</div>

<header class="abs header">
  <div class="brand">
    <div class="brand-mark" role="img" aria-label="Map of Australia brand mark"></div>
    <div>
      <div class="brand-name">Lanternbugs</div>
      <div class="brand-tagline">Inquisitive minds on adventure</div>
    </div>
  </div>
  <nav class="nav">
    <span class="active">HOME</span><span>ABOUT US</span><span>ACTIVITIES</span><span class="tab-calendar">CALENDAR</span><span>CONTACT US</span>
    <svg width="11" height="11" viewBox="0 0 11 11"><circle cx="4.5" cy="4.5" r="3.5" stroke="#333" stroke-width="1.6" fill="none"/><path d="M7 7l3.5 3.5" stroke="#333" stroke-width="1.8"/></svg>
  </nav>
  <div class="subscribe">
    <div class="gift" role="img" aria-label="Gift box icon"></div>
    <div><b>SUBSCRIBE &amp; GET</b><span>weekly activity ideas</span></div>
  </div>
</header>

<div class="abs finder">
  <div class="finder-q">
    <svg width="20" height="20" viewBox="0 0 20 20"><circle cx="10" cy="9" r="5" fill="none" stroke="#0b4e9e" stroke-width="1.6"/><rect x="8" y="14" width="4" height="3" fill="#0b4e9e"/><path d="M10 0v2M2 9H0M20 9h-2M3.5 3l1.4 1.4M16.5 3l-1.4 1.4" stroke="#0b4e9e" stroke-width="1.4"/></svg>
    What to do with your children in Melbourne?
  </div>
  <div class="select">
    <svg width="20" height="18" viewBox="0 0 20 18"><circle cx="5" cy="2.5" r="2.3" fill="#0b4e9e"/><path d="M3 6h4l1 6H6.5v6h-3v-6H2z" fill="#0b4e9e"/><circle cx="14.5" cy="7.5" r="1.8" fill="#e8900c"/><path d="M13 10.5h3l.8 4h-1v3.5h-2.6v-3.5h-1z" fill="#e8900c"/><path d="M7.5 8.5q3 3.5 5.5 2.5" stroke="#555" stroke-width="1.2" fill="none"/></svg>
    <span>Age</span><i class="caret"></i>
  </div>
  <div class="select">
    <svg width="20" height="18" viewBox="0 0 20 18"><path d="M0 18V9h4V5h4v13zM9 18V2h5v16zM15 18v-8h5v8z" fill="#0b4e9e"/><path d="M11 5h1M11 8h1M11 11h1M2 12h1M5 9h1" stroke="#fff" stroke-width="1.2"/></svg>
    <span>Theme</span><i class="caret"></i>
  </div>
  <div class="select">
    <svg width="13" height="17" viewBox="0 0 12 16"><path d="M6 0a6 6 0 0 1 6 6c0 4-6 10-6 10S0 10 0 6a6 6 0 0 1 6-6z" fill="#0b4e9e"/><circle cx="6" cy="6" r="2.2" fill="#fff"/></svg>
    <span>Location</span><i class="caret"></i>
  </div>
  <div class="finder-btn">See Our<br>Suggetions</div>
</div>

<section class="abs hero" role="img" aria-label="Photograph of a mother and young daughter among pink tulips in a field">
  <div class="hero-caption">
    <h2>Explore<br>Bloomfield Tulip Festival</h2>
    <p>A showcase of the Yarra Valley and Dandenong Ranges is on display among the tulips this week.</p>
  </div>
</section>

<div class="abs divider" style="top:554px"></div>

<section class="abs signup">
  <h2>Receive your weekly <em>program of activities</em></h2>
  <h3>Register for free and receive each week:</h3>
  <ul>
    <li><svg width="11" height="9" viewBox="0 0 11 9"><path d="M1 4.5l3 3L10 1" stroke="#0b4e9e" stroke-width="2" fill="none"/></svg>Your personalized program of weekend outings with children</li>
    <li><svg width="11" height="9" viewBox="0 0 11 9"><path d="M1 4.5l3 3L10 1" stroke="#0b4e9e" stroke-width="2" fill="none"/></svg>Programs of activities to occupy your children during the holidays</li>
    <li><svg width="11" height="9" viewBox="0 0 11 9"><path d="M1 4.5l3 3L10 1" stroke="#0b4e9e" stroke-width="2" fill="none"/></svg>Exclusive offers on a selection of activities</li>
  </ul>
  <div class="signup-form">
    <span style="width:250px">Enter mail id</span>
    <span style="width:124px">Postal Code</span>
    <span class="btn">SUBMIT</span>
  </div>
</section>
<div class="abs mailbox" role="img" aria-label="Illustration of a letterbox stuffed with mail standing on grass"></div>

<div class="abs divider" style="top:826px"></div>

<div class="abs promo promo-blue">
  <div class="art" role="img" aria-label="Illustration of a light bulb idea character" style="background:radial-gradient(circle,#3f7fd0,#0b4e9e)"></div>
  <div class="txt"><p>Receive our activity ideas once a week!</p><span class="pill">I am registering</span></div>
</div>
<div class="abs promo promo-orange">
  <div class="art" role="img" aria-label="Illustration of children sharing a laptop" style="background:radial-gradient(circle,#fbc46a,#e8900c)"></div>
  <div class="txt"><p>Use your favorite social network to log in!</p><span class="pill">Log in now</span></div>
</div>
<div class="abs promo promo-dark">
  <div class="txt"><h4>The Lanternbugs Card</h4><p>Get 50% discount<br>on your activities!</p><span class="pill">Get my card</span></div>
  <div class="art" role="img" aria-label="Illustration of an orange gift box"></div>
</div>

<div class="abs divider" style="top:992px"></div>

<h2 class="abs section-title" style="left:190px;top:1014px">Upcoming <em>Events</em></h2>
<p class="abs subheading" style="left:190px;top:1051px">Lanternbugs selections of the month</p>

<article class="abs event" style="left:190px;top:1076px">
  <div class="photo" role="img" aria-label="Photo of a dinosaur skeleton exhibit in a museum hall" style="background:linear-gradient(135deg,#3a3a3a,#7a6a52 50%,#2b2b2b)"></div>
  <div class="body"><h3>Sed ut perspiciatis unde omnis iste natus error sit volupta</h3>
  <div class="meta"><span><svg width="9" height="9" viewBox="0 0 9 9"><rect x=".5" y="1.5" width="8" height="7" fill="none" stroke="#0b4e9e"/><path d="M.5 3.5h8" stroke="#0b4e9e"/></svg>5th Jan</span><span><svg width="9" height="9" viewBox="0 0 9 9"><circle cx="4.5" cy="4.5" r="4" fill="none" stroke="#0b4e9e"/><path d="M4.5 2v2.5h2" stroke="#0b4e9e" fill="none"/></svg>10.30am</span><span><svg width="7" height="9" viewBox="0 0 12 16"><path d="M6 0a6 6 0 0 1 6 6c0 4-6 10-6 10S0 10 0 6a6 6 0 0 1 6-6z" fill="#0b4e9e"/></svg>City Science Hall</span></div>
  <p>Dnventore veritatis et quasi architecto beatae vitae dicta sunt explicabo. Nemo enim ipsam voluptatem quia voluptas sit aspernatur aut odit aut fugit.</p><span class="more">Know more</span></div>
</article>
<article class="abs event" style="left:473px;top:1076px">
  <div class="photo" role="img" aria-label="Photo of two girls playing with a hula hoop outdoors" style="background:linear-gradient(135deg,#5d8a4a,#d9a3b4 55%,#3f6a9a)"></div>
  <div class="body"><h3>Excepteur sint occaecat cupid atat non proident sunt in</h3>
  <div class="meta"><span><svg width="9" height="9" viewBox="0 0 9 9"><rect x=".5" y="1.5" width="8" height="7" fill="none" stroke="#0b4e9e"/><path d="M.5 3.5h8" stroke="#0b4e9e"/></svg>24th Jan</span><span><svg width="9" height="9" viewBox="0 0 9 9"><circle cx="4.5" cy="4.5" r="4" fill="none" stroke="#0b4e9e"/><path d="M4.5 2v2.5h2" stroke="#0b4e9e" fill="none"/></svg>11.00am</span><span><svg width="7" height="9" viewBox="0 0 12 16"><path d="M6 0a6 6 0 0 1 6 6c0 4-6 10-6 10S0 10 0 6a6 6 0 0 1 6-6z" fill="#0b4e9e"/></svg>Riverside Park</span></div>
  <p>ullamco laboris nisi ut aliquip ex ea com modo consequat. Duis aute irure dolor in reprehenderit in voluptate velit esse cillu dolore eu fugiat.</p><span class="more">Know more</span></div>
</article>
<article class="abs event" style="left:757px;top:1076px">
  <div class="photo" role="img" aria-label="Photo of children in chef hats at a cooking class" style="background:linear-gradient(135deg,#c98c66,#eeeeee 45%,#b23a2e)"></div>
  <div class="body"><h3>Lorem ipsum dolorsectetur adipisci proident sunt in</h3>
  <div class="meta"><span><svg width="9" height="9" viewBox="0 0 9 9"><rect x=".5" y="1.5" width="8" height="7" fill="none" stroke="#0b4e9e"/><path d="M.5 3.5h8" stroke="#0b4e9e"/></svg>03rd Feb</span><span><svg width="9" height="9" viewBox="0 0 9 9"><circle cx="4.5" cy="4.5" r="4" fill="none" stroke="#0b4e9e"/><path d="M4.5 2v2.5h2" stroke="#0b4e9e" fill="none"/></svg>08.30am</span><span><svg width="7" height="9" viewBox="0 0 12 16"><path d="M6 0a6 6 0 0 1 6 6c0 4-6 10-6 10S0 10 0 6a6 6 0 0 1 6-6z" fill="#0b4e9e"/></svg>Willow Bend Park</span></div>
  <p>Duis aute irure dolor in ullamco laboris nisi ut aliquip ex ea com modo conse quat. reprehenderit in voluptate velit esse cillu dolore eu fugiat.</p><span class="more">Know more</span></div>
</article>

<article class="abs event" style="left:190px;top:1510px">
  <div class="photo" role="img" aria-label="Photo of children ice skating with an adult" style="background:linear-gradient(180deg,#b8b8b8,#e6e8ec 60%,#cfd4da)"></div>
  <div class="body"><h3>Sed ut perspiciatis unde omnis iste natus error sit volupta</h3>
  <div class="meta"><span><svg width="9" height="9" viewBox="0 0 9 9"><rect x=".5" y="1.5" width="8" height="7" fill="none" stroke="#0b4e9e"/><path d="M.5 3.5h8" stroke="#0b4e9e"/></svg>5th Jan</span><span><svg width="9" height="9" viewBox="0 0 9 9"><circle cx="4.5" cy="4.5" r="4" fill="none" stroke="#0b4e9e"/><path d="M4.5 2v2.5h2" stroke="#0b4e9e" fill="none"/></svg>10.30am</span><span><svg width="7" height="9" viewBox="0 0 12 16"><path d="M6 0a6 6 0 0 1 6 6c0 4-6 10-6 10S0 10 0 6a6 6 0 0 1 6-6z" fill="#0b4e9e"/></svg>City Science Hall</span></div>
  <p>Dnventore veritatis et quasi architecto beatae vitae dicta sunt explicabo. Nemo enim ipsam voluptatem quia voluptas sit aspernatur aut odit aut fugit.</p><span class="more">Know more</span></div>
</article>
<article class="abs event" style="left:473px;top:1510px">
  <div class="photo" role="img" aria-label="Photo of young children feeding a deer at a wildlife park" style="background:linear-gradient(135deg,#3f6b2c,#9c7a52 55%,#5c8c3a)"></div>
  <div class="body"><h3>Excepteur sint occaecat cupid atat non proident sunt in</h3>
  <div class="meta"><span><svg width="9" height="9" viewBox="0 0 9 9"><rect x=".5" y="1.5" width="8" height="7" fill="none" stroke="#0b4e9e"/><path d="M.5 3.5h8" stroke="#0b4e9e"/></svg>24th Jan</span><span><svg width="9" height="9" viewBox="0 0 9 9"><circle cx="4.5" cy="4.5" r="4" fill="none" stroke="#0b4e9e"/><path d="M4.5 2v2.5h2" stroke="#0b4e9e" fill="none"/></svg>11.00am</span><span><svg width="7" height="9" viewBox="0 0 12 16"><path d="M6 0a6 6 0 0 1 6 6c0 4-6 10-6 10S0 10 0 6a6 6 0 0 1 6-6z" fill="#0b4e9e"/></svg>Riverside Park</span></div>
  <p>ullamco laboris nisi ut aliquip ex ea com modo consequat. Duis aute irure dolor in reprehenderit in voluptate velit esse cillu dolore eu fugiat.</p><span class="more">Know more</span></div>
</article>
<article class="abs event" style="left:757px;top:1510px">
  <div class="photo" role="img" aria-label="Photo of a child looking through a magnifying glass on grass" style="background:linear-gradient(135deg,#6aa23a,#b8884e 50%,#4f8a2a)"></div>
  <div class="body"><h3>Lorem ipsum dolorsectetur adipisci proident sunt in</h3>
  <div class="meta"><span><svg width="9" height="9" viewBox="0 0 9 9"><rect x=".5" y="1.5" width="8" height="7" fill="none" stroke="#0b4e9e"/><path d="M.5 3.5h8" stroke="#0b4e9e"/></svg>03rd Feb</span><span><svg width="9" height="9" viewBox="0 0 9 9"><circle cx="4.5" cy="4.5" r="4" fill="none" stroke="#0b4e9e"/><path d="M4.5 2v2.5h2" stroke="#0b4e9e" fill="none"/></svg>08.30am</span><span><svg width="7" height="9" viewBox="0 0 12 16"><path d="M6 0a6 6 0 0 1 6 6c0 4-6 10-6 10S0 10 0 6a6 6 0 0 1 6-6z" fill="#0b4e9e"/></svg>Willow Bend Park</span></div>
  <p>Duis aute irure dolor in ullamco laboris nisi ut aliquip ex ea com modo conse quat. reprehenderit in voluptate velit esse cillu dolore eu fugiat.</p><span class="more">Know more</span></div>
</article>

<div class="abs divider" style="top:1963px"></div>
<div class="abs show-more">Show<br>More</div>

<h2 class="abs section-title" style="left:0;width:1200px;text-align:center;top:2016px">Latest <em>Blogs</em></h2>

<article class="abs blog" style="left:225px;top:2075px">
  <div class="photo" role="img" aria-label="Photo of girls singing into a microphone in a music room" style="background:linear-gradient(135deg,#8a6a58,#d6b49a 50%,#c04a7a)"><div class="date"><b>25</b><span>Nov</span></div></div>
  <div class="body"><h3>Dotam rem aperiam, eaque ipsa</h3>
  <p>Nemo enim ipsam voluptatem quia voluptas sit aspernatur aut odit aut fugit, sed quia consequuntur magni dolores eos qui ratione voluptatem sequi nesciunt.</p><span class="more">Read more</span></div>
</article>
<article class="abs blog" style="left:637px;top:2075px">
  <div class="photo" role="img" aria-label="Photo of children playing ball games in a school gym" style="background:linear-gradient(180deg,#c8c2b8,#c98e52 55%,#a86a34)"><div class="date"><b>25</b><span>Nov</span></div></div>
  <div class="body"><h3>Sed do eiusmod tempor incididunt</h3>
  <p>Nemo enim ipsam voluptatem quia voluptas sit aspernatur aut odit aut fugit, sed quia consequuntur magni dolores eos qui ratione voluptatem sequi nesciunt.</p><span class="more">Read more</span></div>
</article>

<footer class="abs footer">
  <div class="abs contact">
    <h4>Contact us</h4>
    <ul>
      <li><svg width="8" height="11" viewBox="0 0 12 16"><path d="M6 0a6 6 0 0 1 6 6c0 4-6 10-6 10S0 10 0 6a6 6 0 0 1 6-6z" fill="#ddd"/></svg>48 Wattle Row, Bayside, VIC 3207</li>
      <li><svg width="10" height="10" viewBox="0 0 10 10"><path d="M2 0l2 2.5-1.2 1.3c.8 1.5 1.9 2.6 3.4 3.4L7.5 6 10 8l-1.5 2C4 9.5.5 6 0 1.5z" fill="#ddd"/></svg>+(000) 000-0000</li>
      <li><svg width="11" height="8" viewBox="0 0 11 8"><rect width="11" height="8" fill="#ddd"/><path d="M0 0l5.5 4.5L11 0" stroke="#3b3b3b" fill="none"/></svg>contact@lanternbugs.com.au</li>
    </ul>
    <hr>
    <div class="socials"><i></i><i></i><i></i><i></i></div>
  </div>
  <div class="abs insta">
    <h4>Instagram</h4>
    <div class="grid">
      <div role="img" aria-label="Photo of children playing outdoors" style="background:#6f8f4a"></div>
      <div role="img" aria-label="Photo of children doing crafts" style="background:#a85a4a"></div>
      <div role="img" aria-label="Photo of a playground" style="background:#8a8478"></div>
      <div role="img" aria-label="Photo of kids at a class" style="background:#b79a7a"></div>
      <div role="img" aria-label="Photo of a family outing" style="background:#5f7ea0"></div>
      <div role="img" aria-label="Photo of children reading" style="background:#7a6a5a"></div>
    </div>
  </div>
  <div class="abs widget">
    <div class="cover" role="img" aria-label="Page cover photo of children at an activity"></div>
    <div class="bar"><span>Like Page</span><span>Share</span></div>
    <p>Be the first of your friends to like this</p>
    <div class="faces"><i></i><i></i><i></i><i></i><i></i><i></i><i></i><i></i></div>
  </div>
  <div class="abs foot-rule"></div>
  <div class="abs copyright">Copyright © Lanternbugs Melbourne 2016</div>
</footer>
</body>
</html>
```